Love Your Hearing - Life Sounds Good

I need a website. I had a company doing it, and it looked very nice, but they went way up on hosting costs and said they owned the design of the site. I changed hosts to keep costs down. You can see the current design at crestvaleaudio.com. They said I could use the copy and images from the current website. So you could cut and paste to speed things up. My logo and other images are on the current website. If you are unable to use I can send other digital copies.

Target Market(s)

seniors 55 and up

Number of Pages Required

4 page

Font styles to use
Sans Serif

Colors
0255a3
f78f20

Requirements
Must have
• Video testimonies that I can add without assistance. I use youtube links for the videos.
Nice to have
• The color scheme theme can be drawn from the logo, which is on the current webstie crestvaleaudio.com
Should not have
• Should not have anything related to SonoPath on the website.

```html
<!DOCTYPE html>
<html lang="en">
<head>
<meta charset="utf-8">
<title>Crestvale Hearing Center</title>
<link rel="stylesheet" href="https://fonts.googleapis.com/css2?family=Cinzel:wght@600;700&family=Montserrat:wght@400;600&family=Mulish:wght@400;600;700&display=swap">
<style>
:root{
  --blue:#0255a3;
  --blue-dark:#0a3f7a;
  --orange:#f78f20;
  --orange-deep:#ee7a10;
  --ink:#333;
  --muted:#777;
  --grey-bg:#f2f4f8;
  --white:#fff;
}
*{margin:0;padding:0;box-sizing:border-box}
html,body{width:1200px;height:4203px;overflow:hidden;background:var(--white)}
body{position:relative;font-family:'Mulish',sans-serif;color:var(--ink)}
.abs{position:absolute}
.serif{font-family:'Cinzel',serif;font-weight:700;letter-spacing:1px}
.btn{position:absolute;display:flex;align-items:center;justify-content:center;border-radius:30px;color:var(--white);font-family:'Cinzel',serif;font-weight:700;font-size:19px;letter-spacing:1px}
.btn.orange{background:var(--orange)}
.btn.blue{background:var(--blue)}
.accent{color:var(--orange)}
.heading{position:absolute;left:0;width:1200px;text-align:center;font-family:'Cinzel',serif;font-weight:700;font-size:44px;color:var(--blue);letter-spacing:1px}

/* header + hero */
.hero-photo{position:absolute;left:0;top:0;width:1200px;height:690px;background:linear-gradient(120deg,#3d3f42 0%,#5d5a52 40%,#7a5d4a 65%,#4a4540 100%)}
.nav{position:absolute;top:84px;font-family:'Montserrat',sans-serif;font-size:13px;color:var(--white)}
.nav span{position:absolute;white-space:nowrap}
.nav .active{color:var(--orange)}
.nav-line{position:absolute;top:62px;height:1px;background:rgba(255,255,255,.35)}
.phone{position:absolute;left:893px;top:14px;display:flex;align-items:center;gap:12px;color:var(--orange);font-family:'Cinzel',serif;font-size:23px;font-weight:600}
.phone i{width:34px;height:34px;border-radius:50%;background:var(--blue);display:flex;align-items:center;justify-content:center}
.brand{position:absolute;left:485px;top:36px;display:flex;align-items:center;gap:10px}
.brand .mark{width:54px;height:54px;background:var(--orange)}
.brand .name{font-family:'Cinzel',serif;font-weight:700;color:var(--orange);font-size:17px;line-height:1.1}
.hero-title{position:absolute;left:77px;top:228px;font-family:'Montserrat',sans-serif;font-weight:600;font-size:51px;line-height:57px;color:var(--white)}
.hero-sub{position:absolute;left:80px;top:352px;font-family:'Montserrat',sans-serif;font-size:21px;color:var(--white)}

/* services */
.svc{position:absolute;top:580px;width:240px;text-align:center}
.svc .ring{margin:0 auto;width:168px;height:168px;border-radius:50%;background:var(--white);display:flex;align-items:center;justify-content:center;border:5px solid var(--blue)}
.svc.o .ring{border-color:var(--orange)}
.svc .disc{width:146px;height:146px;border-radius:50%;background:radial-gradient(circle at 40% 35%,#2f7fcf,var(--blue));display:flex;align-items:center;justify-content:center}
.svc.o .disc{background:radial-gradient(circle at 40% 35%,#ffab4a,var(--orange-deep))}
.svc h3{font-family:'Cinzel',serif;font-weight:700;color:var(--blue);font-size:19px;line-height:27px;letter-spacing:1px}
.svc p{font-size:13px;line-height:26px;color:var(--muted);margin-top:10px}

/* schedule band */
.sched-title{position:absolute;left:0;width:1200px;top:1232px;text-align:center;color:var(--white);font-family:'Cinzel',serif;font-weight:600;font-size:42px;letter-spacing:2px}
.sched-sub{position:absolute;left:0;width:1200px;top:1297px;text-align:center;color:var(--white);font-family:'Montserrat',sans-serif;font-size:24px}

/* testimonial */
.quote{position:absolute;left:130px;top:1702px;width:460px;text-align:right;font-style:italic;font-size:18px;line-height:31px;color:#444}
.quote-name{position:absolute;left:300px;top:1780px;width:292px;text-align:right;font-family:'Montserrat',sans-serif;font-weight:600;color:var(--orange);font-size:21px}
.dots{position:absolute;left:462px;top:1841px;display:flex;gap:7px}
.dots span{width:13px;height:13px;border-radius:50%;border:1.5px solid var(--blue)}
.dots .on{background:var(--orange);border-color:var(--orange)}

/* ways */
.ways{position:absolute;left:0;top:1981px;width:1200px;height:470px;background:var(--grey-bg)}
.way{position:absolute;top:2134px;width:198px;height:213px;background:var(--white);box-shadow:0 2px 8px rgba(0,0,0,.06);text-align:center}
.way svg{margin-top:40px}
.way p{position:absolute;left:0;right:0;top:132px;font-weight:700;font-size:15px;line-height:24px;color:var(--blue)}

/* welcome */
.welcome h2{position:absolute;left:671px;top:2526px;font-family:'Cinzel',serif;font-weight:700;font-size:44px;color:var(--white);letter-spacing:1px}
.welcome h3{position:absolute;left:676px;top:2583px;font-family:'Cinzel',serif;font-weight:600;font-size:22px;color:var(--orange);letter-spacing:1px}
.welcome p{position:absolute;left:676px;top:2628px;width:440px;font-size:13.5px;line-height:27px;color:var(--white)}

/* news */
.news{position:absolute;top:3046px;width:311px;height:384px;background:var(--white);box-shadow:0 2px 10px rgba(0,0,0,.07);text-align:center}
.news .pic{margin:11px auto 0;width:291px;height:193px}
.news h4{margin-top:38px;font-family:'Cinzel',serif;font-weight:700;font-size:16px;line-height:27px;color:var(--blue);letter-spacing:1px;padding:0 24px}
.news .date{margin-top:13px;font-family:'Montserrat',sans-serif;font-weight:600;font-size:13px;color:var(--orange)}

/* footer */
.foot-h{position:absolute;top:3858px;font-family:'Cinzel',serif;font-weight:700;font-size:18px;color:var(--white);letter-spacing:1px}
.foot-list{position:absolute;top:3900px;list-style:none;font-size:13px;line-height:29.3px;color:var(--white)}
.foot-list li::before{content:"";display:inline-block;width:6px;height:6px;border-radius:50%;background:var(--orange);margin-right:14px;vertical-align:middle}
.contact{position:absolute;right:76px;text-align:right;color:var(--white);font-size:13.5px;line-height:22px;display:flex;align-items:center;gap:14px}
.social{position:absolute;top:4047px;right:75px;display:flex;gap:9px}
.social span{width:38px;height:38px;border-radius:50%}
.copy{position:absolute;left:0;top:4164px;width:1200px;text-align:center;color:var(--white);font-size:12.5px}
</style>
</head>
<body>

<!-- Hero -->
<div class="hero-photo" role="img" aria-label="Photo of a smiling couple with a red kayak at a lakeside"></div>
<div class="nav-line" style="left:72px;width:386px"></div>
<div class="nav-line" style="left:742px;width:381px"></div>
<div class="abs" style="left:152px;top:60px;width:52px;height:3px;background:var(--orange)"></div>
<nav class="nav">
  <span class="active" style="left:159px">HOME</span>
  <span style="left:238px">HEARING AIDS</span>
  <span style="left:376px">SERVICES</span>
  <span style="left:755px">EDUCATION</span>
  <span style="left:865px">ABOUT US</span>
  <span style="left:972px">NEWS</span>
  <span style="left:1042px">CONTACT</span>
</nav>
<div class="phone"><i><svg width="16" height="16" viewBox="0 0 24 24"><path fill="#fff" d="M6.6 10.8a15.1 15.1 0 006.6 6.6l2.2-2.2c.3-.3.7-.4 1-.2 1.1.4 2.3.6 3.6.6.6 0 1 .4 1 1V20c0 .6-.4 1-1 1A17 17 0 013 4c0-.6.4-1 1-1h3.5c.6 0 1 .4 1 1 0 1.3.2 2.5.6 3.6.1.3 0 .7-.2 1z"/></svg></i>(555) 214 - 3380</div>
<div class="brand"><span class="mark"></span><span class="name">CRESTVALE<br>HEARING CENTER</span></div>
<h1 class="hero-title">Recapture The<br>Sounds Of Life</h1>
<p class="hero-sub">And the intimacy of a quiet conversation</p>
<div class="btn blue" style="left:77px;top:400px;width:290px;height:54px;font-size:21px">TAKE ACTION TODAY</div>

<svg class="abs" style="left:0;top:590px" width="1200" height="110" viewBox="0 0 1200 110">
  <path d="M0 16 Q600 110 1200 16 L1200 110 L0 110Z" fill="var(--orange)"/>
  <path d="M0 34 Q600 118 1200 34 L1200 110 L0 110Z" fill="#fff"/>
</svg>

<!-- Services -->
<div class="svc" style="left:78px">
  <div class="ring"><div class="disc"><svg width="64" height="64" viewBox="0 0 64 64" fill="none" stroke="#fff" stroke-width="3"><path d="M24 40c0-14 6-24 16-24s14 8 14 15c0 9-9 10-9 18 0 5-4 8-8 8"/><path d="M14 28q-4 6 0 12M8 24q-6 10 0 20"/></svg></div></div>
  <h3 style="margin-top:20px">HEARING<br>EVALUATIONS</h3>
  <p>The hearing test is a vital part of the process of measuring and fitting hearing aids. Without an accurate assessment.</p>
</div>
<div class="svc o" style="left:350px">
  <div class="ring"><div class="disc"><svg width="64" height="64" viewBox="0 0 64 64" fill="none" stroke="#fff" stroke-width="3"><rect x="12" y="12" width="40" height="40" rx="5"/><rect x="20" y="18" width="24" height="22"/><circle cx="32" cy="46" r="2"/></svg></div></div>
  <h3 style="margin-top:46px">VIDEO<br>OCTOSCOPY</h3>
  <p>Seeing in the ear canal to determine the condition of the skin and tympanic membrane (eardrum) is also crucial.</p>
</div>
<div class="svc" style="left:611px">
  <div class="ring"><div class="disc"><svg width="64" height="64" viewBox="0 0 64 64" fill="none" stroke="#fff" stroke-width="3"><path d="M22 38c0-14 6-24 16-24s14 8 14 15c0 9-9 10-9 18"/><circle cx="37" cy="30" r="5"/><path d="M22 38q-6 8 2 14"/></svg></div></div>
  <h3 style="margin-top:46px">HEARING<br>AID FITTING</h3>
  <p>The first fit is established for the patient using information from the audiogram and the software provided by the.</p>
</div>
<div class="svc o" style="left:884px">
  <div class="ring"><div class="disc"><svg width="64" height="64" viewBox="0 0 64 64" fill="none" stroke="#fff" stroke-width="3"><rect x="12" y="28" width="10" height="24"/><path d="M22 30l8-14c2-4 7-2 6 2l-2 8h12c3 0 5 3 4 6l-4 14c-1 3-3 4-6 4H22"/></svg></div></div>
  <h3 style="margin-top:20px">FOLLOW UP<br>SERVICES</h3>
  <p>All hearing aids require routine service through daily cleanings and either annual or semi-annual visits to the clinic.</p>
</div>
<div class="btn orange" style="left:116px;top:954px;width:170px;height:52px">LEARN MORE</div>
<div class="btn blue" style="left:383px;top:980px;width:170px;height:52px">LEARN MORE</div>
<div class="btn orange" style="left:649px;top:980px;width:170px;height:52px">LEARN MORE</div>
<div class="btn blue" style="left:917px;top:954px;width:170px;height:52px">LEARN MORE</div>

<!-- Schedule -->
<svg class="abs" style="left:0;top:1110px" width="1200" height="410" viewBox="0 0 1200 410" role="img" aria-label="Orange-toned photo of a couple embracing">
  <defs><linearGradient id="schedFill" x1="0" x2="1"><stop offset="0" stop-color="#f07d14"/><stop offset=".5" stop-color="#f59a3c"/><stop offset="1" stop-color="#f78f20"/></linearGradient></defs>
  <path d="M0 82 Q600 -70 1200 76 L1200 330 Q600 470 0 326Z" fill="url(#schedFill)"/>
</svg>
<h2 class="sched-title">SCHEDULE AN APPOINTMENT</h2>
<p class="sched-sub">Take action! Make an appointment for a hearing evaluation</p>
<div class="btn blue" style="left:448px;top:1355px;width:270px;height:57px;font-size:21px">GET APPOINTMENT</div>

<!-- Testimonials -->
<h2 class="heading" style="top:1565px">WHAT OUR <span class="accent">CLIENT SAY</span></h2>
<p class="quote">“If you need hearing aids or have a hearing problem, come see Dan Porter.”</p>
<p class="quote-name">Ray Holloway &nbsp;<span style="display:inline-block;width:18px;height:2px;background:var(--orange);vertical-align:middle"></span></p>
<div class="dots"><span></span><span></span><span class="on"></span><span></span><span></span><span></span><span></span></div>
<div class="abs" style="left:651px;top:1658px;width:250px;height:250px;border-radius:50%;border:6px solid var(--blue);background:linear-gradient(135deg,#d9cfc2,#a89583 60%,#7d6b5c)" role="img" aria-label="Video testimonial still of two smiling men in an office"></div>
<svg class="abs" style="left:742px;top:1749px" width="68" height="68" viewBox="0 0 68 68"><circle cx="34" cy="34" r="32" fill="var(--orange)"/><path d="M27 21l22 13-22 13z" fill="#fff"/></svg>

<!-- 50 ways -->
<section class="ways"></section>
<h2 class="heading" style="top:2040px">50 WAYS TO LOVE <span class="accent">YOUR HEARING</span></h2>
<div class="way" style="left:77px"><svg width="60" height="60" viewBox="0 0 60 60" fill="none" stroke="var(--orange)" stroke-width="2"><path d="M22 40c0-15 6-26 16-26s14 8 14 15c0 9-9 10-9 18 0 5-4 8-8 8"/><path d="M12 30q-4 6 0 12"/></svg><p>Bi - Annual Hearing<br>Checkups</p></div>
<div class="way" style="left:289px"><svg width="60" height="60" viewBox="0 0 60 60" fill="none" stroke="var(--orange)" stroke-width="2"><path d="M18 40c0-15 6-26 16-26s14 8 14 15c0 9-9 10-9 18 0 5-4 8-8 8"/><path d="M28 30c0-6 10-6 10 0"/></svg><p>20 db Hearing<br>Checups</p></div>
<div class="way" style="left:501px"><svg width="60" height="60" viewBox="0 0 60 60" fill="none" stroke="var(--orange)" stroke-width="2"><ellipse cx="30" cy="28" rx="24" ry="17"/><path d="M18 43l-6 9 14-6"/><circle cx="20" cy="28" r="3"/><circle cx="30" cy="28" r="3"/><circle cx="40" cy="28" r="3"/></svg><p>Quiet<br>Conversation</p></div>
<div class="way" style="left:713px"><svg width="60" height="60" viewBox="0 0 60 60" fill="none" stroke="var(--orange)" stroke-width="2"><circle cx="20" cy="40" r="11"/><circle cx="20" cy="40" r="3"/><path d="M27 33l20-20M44 8l8 8"/></svg><p>Music</p></div>
<div class="way" style="left:925px"><svg width="60" height="60" viewBox="0 0 60 60" fill="none" stroke="var(--orange)" stroke-width="2"><circle cx="32" cy="10" r="5"/><path d="M30 18l-4 16 10 8-4 14M26 34l-12 12M30 22l-14-6M32 22l14-8"/></svg><p>Dancing</p></div>

<!-- Welcome -->
<section class="welcome">
  <svg class="abs" style="left:0;top:2410px" width="1200" height="540" viewBox="0 0 1200 540">
    <defs><linearGradient id="photoFill" x1="0" y1="0" x2="1" y2="1"><stop offset="0" stop-color="#c8ccd0"/><stop offset=".55" stop-color="#a89a8c"/><stop offset="1" stop-color="#d6d2cc"/></linearGradient></defs>
    <path d="M0 12 Q300 40 600 56 L600 520 L0 520Z" fill="url(#photoFill)" role="img" aria-label="Photo of a grandfather and grandson playing in the sand on a beach"/>
    <path d="M600 56 Q900 40 1200 2 L1200 520 L600 520Z" fill="var(--blue)"/>
    <path d="M0 525 Q600 430 1200 470 L1200 540 L0 540Z" fill="var(--orange)"/>
    <path d="M0 540 Q600 450 1200 495 L1200 540Z" fill="#fff"/>
  </svg>
  <h2>WELCOME TO</h2>
  <h3>CRESTVALE HEARING CENTER LLC</h3>
  <p>We provide hearing evaluations, counseling, and fitting of hearing aids. We service all the major brands of hearing aids including Auralis, Tonewell, Clearwave, Verano, Sonella, Halden, Brightear, Norvale, Quillon, Maris, Pellham, and others.</p>
  <div class="btn orange" style="left:679px;top:2755px;width:198px;height:52px;font-size:21px">LEARN MORE</div>
</section>

<!-- News -->
<h2 class="heading" style="top:2962px">LATEST <span class="accent">NEWS</span></h2>
<article class="news" style="left:101px">
  <div class="pic" style="background:linear-gradient(135deg,#b9a488,#e6e1da 55%,#8aa0b4)" role="img" aria-label="Photo of a woman in sunglasses at a seaside cafe"></div>
  <h4>DO'S AND DON'TS FOR COMMUNICATING DURING THE HOLIDAYS</h4>
  <p class="date">19 DECEMBER 2018</p>
</article>
<article class="news" style="left:444px">
  <div class="pic" style="background:linear-gradient(160deg,#5d6a6e,#9aa69c 60%,#6d7a6a)" role="img" aria-label="Photo of an older woman raising her arms outdoors"></div>
  <h4>COMMUNICATION FOR ALL: HOW PEOPLE OF ALL AGES BENEFIT FROM.</h4>
  <p class="date">01 JUNE 2018</p>
</article>
<article class="news" style="left:789px">
  <div class="pic" style="background:linear-gradient(135deg,#2c2420,#6b4a30 60%,#3a2a22)" role="img" aria-label="Photo of a hand using a card payment terminal"></div>
  <h4>OVER-THE-COUNTER HEARING AIDS: WHAT YOU NEED TO KNOW</h4>
  <p class="date">14 SEPTEMBER 2017</p>
</article>

<!-- Tips -->
<h2 class="heading" style="top:3508px">TIP FOR <span class="accent">WEAREAR</span></h2>
<p class="abs" style="left:0;top:3568px;width:1200px;text-align:center;font-size:17px;color:#555">Tips for Hearing Aid Wearers and Family Members</p>
<div class="btn blue" style="left:514px;top:3620px;width:170px;height:51px;font-size:20px">GET TIPS</div>

<!-- Footer -->
<svg class="abs" style="left:0;top:3700px" width="1200" height="503" viewBox="0 0 1200 503">
  <path d="M0 4 Q600 110 1200 4 L1200 503 L0 503Z" fill="var(--orange)"/>
  <path d="M0 26 Q600 126 1200 26 L1200 503 L0 503Z" fill="var(--blue)"/>
  <circle cx="600" cy="88" r="64" fill="#fff"/>
  <rect x="570" y="58" width="60" height="60" fill="var(--orange)"/>
</svg>
<h4 class="foot-h" style="left:78px">SITEMAP</h4>
<h4 class="foot-h" style="left:256px">SERVICES</h4>
<h4 class="foot-h" style="left:469px">CITY</h4>
<h4 class="foot-h" style="left:990px">CONTACT US</h4>
<ul class="foot-list" style="left:75px"><li>Home</li><li>Hearing Aids</li><li>Services</li><li>Education</li><li>About Us</li><li>News</li><li>Contact Us</li></ul>
<ul class="foot-list" style="left:256px"><li>Hearing Evaluations</li><li>Video Otoscopy</li><li>Hearing Aid Fitting</li><li>Follow Up Service</li><li>Ear Molds</li><li>Wireless Technology</li><li>Tinnitus Treatment</li></ul>
<ul class="foot-list" style="left:467px"><li>Ashby</li><li>Milford Glen</li><li>Dunmore</li><li>Corwin</li><li>Laurel Bend</li><li>Redbrook</li><li>More</li></ul>
<div class="contact" style="top:3902px"><span>240 W. Elm St Suite 18<br>Crestvale, NC 28099</span><svg width="18" height="24" viewBox="0 0 18 24"><path d="M9 0a9 9 0 00-9 9c0 7 9 15 9 15s9-8 9-15a9 9 0 00-9-9z" fill="var(--orange)"/><circle cx="9" cy="9" r="3.5" fill="var(--blue)"/></svg></div>
<div class="contact" style="top:3966px;font-weight:700"><span>1(555) 214-3380</span><svg width="20" height="20" viewBox="0 0 24 24"><path fill="var(--orange)" d="M6.6 10.8a15.1 15.1 0 006.6 6.6l2.2-2.2c.3-.3.7-.4 1-.2 1.1.4 2.3.6 3.6.6.6 0 1 .4 1 1V20c0 .6-.4 1-1 1A17 17 0 013 4c0-.6.4-1 1-1h3.5c.6 0 1 .4 1 1 0 1.3.2 2.5.6 3.6.1.3 0 .7-.2 1z"/></svg></div>
<div class="contact" style="top:4005px;font-weight:700;font-style:italic;text-decoration:underline"><span>Send Us Message</span><svg width="20" height="16" viewBox="0 0 20 16"><rect width="20" height="16" rx="2" fill="var(--orange)"/><path d="M1 2l9 7 9-7" fill="none" stroke="var(--blue)" stroke-width="2"/></svg></div>
<div class="social"><span style="background:#2d4f9a"></span><span style="background:#1fa3e0"></span><span style="background:#c8233a"></span></div>
<p class="copy">© <strong>Crestvale Hearing Center LLC</strong> - 2019. All Rights Reserved</p>

</body>
</html>
```